Pet product line, needs a label design

We are a pharmaceutical company focused on animal health. We have been in the Mexican and Central American market for 10 years. During this time we have developed our line for production animals (beef, poultry, dairy, pigs...) and now we want to develop a line for pets.
Our first product are some pills made of Yucca (Yucca schidigera) which helps the digestive system of cats and dogs improve, reducing gas production and diminishing the bad smell of the pet feces.
We are looking for a design that can represent our new product line using this new product as an example, its name is 'BRONTAVEX'. The brand umbrella is TQ Vira, I am attaching this logo.
We need an attractive and original design with a strong personality, capable of jumping to the eyes of the consumer (pet owner) and also attractive for the Veterinarian who will recommend the product.
We want to highlight the benefits of the product by developing icons to the three main claims of the product.
We hope you will find this project attractive and challenging!!

Target Market(s)

Pet owners (mainly dog and cat)

Veterinarians

Industry/Entity Type

Pharmaceutical

Requirements
Must have
• * Product name (BRONTAVEX)
* Label Information (added in a word document)
* Band umbrella logo TQ Vira
* GREAT DESIGN
* The design should be horizontal (5cm height and 13 cm width)
Nice to have
• Nice product name design

Icon designs for the following claims (in spanish):
+ Limpia el trato digestivo (Cleans the digestive tract)
+ Reduce los malos olores (Reduces odors)
+ Propicia la digestión completa (Promotes complete digestion)

```html
<!DOCTYPE html>
<html lang="es">
<head>
<meta charset="utf-8">
<title>BRONTAVEX – etiqueta</title>
<link rel="stylesheet" href="https://fonts.googleapis.com/css2?family=Baloo+2:wght@800&family=Questrial&family=Quicksand:wght@700&display=swap">
<style>
  :root {
    --teal: #4ec1cc;
    --teal-soft: #bfe8ec;
    --navy: #283591;
    --purple: #9b5fb0;
    --ink: #555866;
    --rule: #7ccfd6;
    --ring-blue: #2f8fd8;
    --ring-green: #6cb33f;
    --ring-orange: #f39a1e;
    --ring-purple: #8e5bb0;
  }
  * { margin: 0; padding: 0; box-sizing: border-box; }
  html, body { width: 1200px; height: 464px; overflow: hidden; background: #fff; }
  .label {
    position: relative; width: 1200px; height: 464px; overflow: hidden;
    font-family: "Questrial", sans-serif; color: var(--ink);
  }
  .bands { position: absolute; inset: 0; }
  .brand {
    position: absolute; display: flex; align-items: center; gap: 8px;
    font-family: "Quicksand", sans-serif; font-weight: 700; color: var(--navy);
  }
  .brand .dot { border-radius: 50%; background: var(--teal); }
  .brand-side { left: 138px; top: 44px; font-size: 24px; }
  .brand-side .dot { width: 16px; height: 16px; }
  .brand-main { left: 560px; top: 66px; font-size: 34px; }
  .brand-main .dot { width: 22px; height: 22px; }

  .info { position: absolute; left: 44px; width: 256px; font-size: 13px; }
  .info h3 {
    font-weight: 400; font-size: 12.5px; color: var(--purple);
    text-transform: uppercase; padding-bottom: 4px; border-bottom: 1px solid var(--rule);
  }
  .info p, .info li { line-height: 20px; border-bottom: 1px solid var(--rule); list-style: none; }
  .dose { top: 100px; }
  .ingredients { top: 178px; }
  .ingredients li::before { content: "- "; }
  .benefits { top: 250px; }
  .benefits li { position: relative; padding-left: 12px; }
  .benefits li::before {
    content: ""; position: absolute; left: 0; top: 6px; width: 7px; height: 7px;
    border-radius: 50%; background: var(--teal);
  }

  .name { position: absolute; left: 438px; top: 40px; width: 130px; height: 400px; }
  .name text { font-family: "Baloo 2", sans-serif; font-weight: 800; fill: var(--navy); }

  .claims { position: absolute; left: 556px; top: 190px; width: 300px; list-style: none; }
  .claims li {
    position: relative; padding-left: 20px; font-size: 16.5px; line-height: 20px;
    color: var(--navy); margin-bottom: 4px;
  }
  .claims svg { position: absolute; left: 0; top: 3px; }

  .icons { position: absolute; left: 562px; top: 309px; display: flex; gap: 8px; }
  .icon {
    width: 56px; height: 56px; border-radius: 50%; border: 5px solid;
    background: radial-gradient(circle, #eaf6fb 40%, #cfe9f2);
  }
  .icon.blue { border-color: var(--ring-blue); }
  .icon.green { border-color: var(--ring-green); }
  .icon.orange { border-color: var(--ring-orange); }
  .icon.purple { border-color: var(--ring-purple); }

  .count {
    position: absolute; left: 652px; top: 408px; width: 136px; height: 32px;
    border: 2px solid var(--teal); border-radius: 16px; text-align: center;
    font-size: 19px; line-height: 28px; color: var(--navy);
  }

  .analysis {
    position: absolute; left: 897px; top: 60px; width: 244px;
    border-collapse: collapse; font-size: 12px;
  }
  .analysis th {
    background: var(--teal); color: #fff; font-weight: 400; font-size: 16px;
    text-align: left; padding: 3px 8px; height: 26px;
  }
  .analysis td { border: 1px solid var(--teal); height: 22.5px; padding: 0 6px; }
  .analysis td.value { width: 102px; text-align: right; }

  .contents, .maker { position: absolute; left: 904px; width: 240px; font-size: 12.5px; }
  .contents { top: 266px; line-height: 16px; }
  .maker { top: 316px; line-height: 20px; }
</style>
</head>
<body>
<div class="label">
  <svg class="bands" width="1200" height="464" viewBox="0 0 1200 464" aria-hidden="true">
    <path d="M0 0H1200V46C1120 46 1000 44 900 44C860 44 850 30 830 22C800 8 760 30 690 30C620 30 560 10 500 22C470 28 460 16 440 16C300 16 120 20 0 20Z" fill="var(--teal)"/>
    <path d="M0 20C120 20 300 16 440 16C420 24 410 30 380 30H0Z" fill="var(--teal-soft)"/>
    <path d="M0 446H1200V464H0Z" fill="var(--teal)"/>
    <path d="M600 446C640 436 760 436 800 446Z" fill="var(--teal)"/>
    <line x1="304" y1="260" x2="304" y2="446" stroke="var(--teal-soft)" stroke-width="1"/>
  </svg>

  <div class="brand brand-side"><span class="dot"></span>TQ Vira</div>

  <section class="info dose">
    <h3>Dosis</h3>
    <p>Mascotas pequeñas 1 tableta al día</p>
    <p>Mascotas grandes 2 tabletas al día</p>
  </section>
  <section class="info ingredients">
    <h3>Ingredientes activos</h3>
    <ul><li>Saponinas</li><li>Glicocomponentes</li></ul>
  </section>
  <section class="info benefits">
    <h3>Beneficios</h3>
    <ul>
      <li>Reduce significativamente los malos olores en los desechos de las mascotas</li>
      <li>Reduce el estrés</li>
      <li>Limpia el tracto digestivo</li>
      <li>Propicia una digestión completa</li>
      <li>Efectos anti-inflamatorios</li>
      <li>Efectos antireumáticos</li>
    </ul>
  </section>

  <svg class="name" viewBox="0 0 130 400" aria-label="BRONTAVEX">
    <text transform="translate(104 395) rotate(-90)" font-size="118" textLength="390" lengthAdjust="spacingAndGlyphs">brontavex</text>
  </svg>

  <div class="brand brand-main"><span class="dot"></span>TQ Vira</div>

  <ul class="claims">
    <li><svg width="14" height="12" viewBox="0 0 14 12"><path d="M1 6l4 4 8-9" fill="none" stroke="var(--navy)" stroke-width="2"/></svg>Reduce significativamente los malos olores en los desechos de las mascotas</li>
    <li><svg width="14" height="12" viewBox="0 0 14 12"><path d="M1 6l4 4 8-9" fill="none" stroke="var(--navy)" stroke-width="2"/></svg>Reduce el estrés</li>
    <li><svg width="14" height="12" viewBox="0 0 14 12"><path d="M1 6l4 4 8-9" fill="none" stroke="var(--navy)" stroke-width="2"/></svg>Limpia el tracto digestivo</li>
  </ul>

  <div class="icons">
    <div class="icon blue" role="img" aria-label="Icono: tracto digestivo limpio"></div>
    <div class="icon green" role="img" aria-label="Icono: mascota sin estrés"></div>
    <div class="icon orange" role="img" aria-label="Icono: reducción de malos olores"></div>
    <div class="icon purple" role="img" aria-label="Icono: digestión completa"></div>
  </div>

  <div class="count">60 Tabletas</div>

  <table class="analysis">
    <tr><th colspan="2">Análisis bromatológico</th></tr>
    <tr><td>Humedad</td><td class="value">Max. 8.2 %</td></tr>
    <tr><td>Proteína Cruda</td><td class="value">Max. 20 %</td></tr>
    <tr><td>Grasa Cruda</td><td class="value">Max. 0.5 %</td></tr>
    <tr><td>Fibra Cruda</td><td class="value">Max. 30.0 %</td></tr>
    <tr><td>Cenizas</td><td class="value">Max. 11.0 %</td></tr>
    <tr><td>Carbohidratos</td><td class="value">Max. 42.5 %</td></tr>
    <tr><td>Excipiente cbp</td><td class="value"></td></tr>
  </table>

  <p class="contents">Contenido: Yucca schidigera extracto pulverizado</p>
  <div class="maker">
    <p>Elaborado para :</p>
    <p>Norvel Animal, S.A. de C.V.</p>
    <p>Av. Tamarindos 2417</p>
    <p>Colinas del Roble</p>
    <p>CP 44390</p>
    <p>Guadalajara, Jal.</p>
  </div>
</div>
</body>
</html>
```